A new art and beauty business needing a eCommerce design

I need an ecommerce design for my company that is based in Australia called 'Fern and Fable'. I make art and other products and would like the website to be an easy to use website, it must however, look modern and professional.

Could you please provide the finished product CODED with HTML etc. and ready to be used.

Colours can be chosen by the designer and are not limited in any way by our previous websites design.

I look forward to your submissions and will reward good work with our approval for payment.

If you would like further information you are welcome to ask.

Industry/Entity Type

Business

Contact Information for Business Card

Company Name: Fern and Fable

Owners Name: Darren Vollmacht

Address: 14 Copperfield Row
Tumbarra, NSW 2687
Australia

Phone: 0491 786 215

Email: contact@fern-andfable.com

Logo Text

Fern and Fable

```html
<!DOCTYPE html>
<html lang="en">
<head>
<meta charset="utf-8">
<title>Fern and Fable</title>
<link href="https://fonts.googleapis.com/css2?family=Oswald:wght@400;600;700&family=Open+Sans:wght@400;600;700&display=swap" rel="stylesheet">
<style>
:root{
  --pink:#d6337a;
  --coral:#f0513e;
  --orange:#f28a1e;
  --teal:#1e8b92;
  --teal-light:#63d6dc;
  --teal-dark:#2d5b60;
  --charcoal:#353535;
  --charcoal-dark:#262626;
  --sage:#8db48c;
  --white:#ffffff;
  --grey-text:#bdbdbd;
  --card-text:#8a8a8a;
}
*{box-sizing:border-box;margin:0;padding:0}
html,body{width:831px;height:1200px;overflow:hidden}
body{font-family:"Open Sans",Arial,sans-serif;color:var(--white);background:var(--charcoal);position:relative}
.btn{display:inline-block;font-family:"Oswald",Arial,sans-serif;font-size:8px;letter-spacing:.5px;text-transform:uppercase;color:var(--white);padding:4px 10px;border-radius:2px;background:var(--coral)}
.btn.teal{background:var(--teal)}
.btn.grey{background:#9a9a9a}

/* hero */
.hero{position:absolute;left:0;top:0;width:831px;height:250px;overflow:hidden}
.hero-photo{position:absolute;inset:0;background:radial-gradient(ellipse at 30% 85%,#b4d08a 0%,rgba(180,208,138,0) 45%),radial-gradient(ellipse at 75% 70%,#e8d2c4 0%,rgba(232,210,196,0) 40%),linear-gradient(180deg,#c5418f 0%,#d98aa8 45%,#cfc0a0 100%)}
.topbar{position:absolute;left:0;top:0;width:831px;height:30px;background:rgba(120,30,90,.55);display:flex;align-items:center;justify-content:space-between;padding:0 150px 0 160px}
.brand{font-family:"Oswald",Arial,sans-serif;font-size:11px;font-weight:600;color:var(--white);background:var(--pink);padding:8px 12px;height:30px;display:flex;align-items:center}
.nav{display:flex;gap:4px;list-style:none}
.nav li{font-size:7px;padding:4px 8px;color:var(--white)}
.nav li.active{background:var(--orange)}
.hero-copy{position:absolute;top:98px;width:831px;text-align:center}
.hero-copy h1{font-family:"Oswald",Arial,sans-serif;font-weight:600;font-size:21px;letter-spacing:1.5px;text-transform:uppercase}
.hero-copy p{font-family:"Oswald",Arial,sans-serif;font-size:14px;letter-spacing:1px;text-transform:uppercase;opacity:.9;margin:4px 0 10px}

/* about */
.about{position:absolute;top:250px;left:0;width:831px;height:170px;background:var(--charcoal);display:flex;justify-content:center;gap:40px;padding-top:24px}
.feature{width:140px;text-align:center}
.feature .icon{width:42px;height:42px;border-radius:50%;background:var(--white);margin:0 auto 8px;display:flex;align-items:center;justify-content:center}
.feature h3{font-family:"Oswald",Arial,sans-serif;font-size:11px;font-weight:600;letter-spacing:.5px}
.feature h3 span{color:var(--teal-light)}
.feature p{font-size:6.5px;line-height:1.5;color:var(--grey-text);margin:5px 0 8px}

/* news */
.news{position:absolute;top:420px;left:0;width:831px;height:222px;background:var(--teal);overflow:hidden}
.news-photo{position:absolute;left:0;top:0;width:831px;height:222px}
.news-panel{position:absolute;left:505px;top:26px;width:290px}
.news-panel h2{font-family:"Oswald",Arial,sans-serif;font-size:22px;font-weight:600;color:var(--teal-light);text-transform:uppercase;margin-bottom:14px}
.news-item{display:flex;gap:10px;margin-bottom:14px}
.date{width:34px;height:34px;background:var(--coral);text-align:center;font-family:"Oswald",Arial,sans-serif;line-height:1}
.date b{display:block;font-size:15px;padding-top:4px}
.date small{font-size:7px}
.news-item p{font-size:7px;line-height:1.45;width:140px}
.news-item a{display:block;color:var(--orange);font-size:7px;font-weight:700;margin-top:3px;text-align:right}

/* services */
.services{position:absolute;top:642px;left:0;width:831px;height:290px;background:var(--sage);text-align:center}
.services h2{font-family:"Oswald",Arial,sans-serif;font-size:17px;font-weight:600;text-transform:uppercase;margin-top:38px}
.services .sub{font-size:6.5px;opacity:.85;margin-top:3px}
.services .rule{width:120px;height:1px;background:rgba(255,255,255,.6);margin:5px auto 0}
.cards{display:flex;justify-content:center;gap:32px;margin-top:34px}
.card{width:142px;height:162px;background:var(--white);border-top:3px solid var(--coral);padding-top:14px}
.card.dark{border-top-color:var(--charcoal)}
.card.teal{border-top-color:var(--teal)}
.card .thumb{width:78px;height:78px;border-radius:50%;margin:0 auto}
.card p{font-size:6px;line-height:1.5;color:var(--card-text);margin:8px 14px 8px}

/* offers */
.offers{position:absolute;top:932px;left:0;width:831px;height:180px;background:radial-gradient(ellipse at 50% 40%,#3a3a3a 0%,#1e1e1e 70%)}
.offer{position:absolute;top:30px;display:flex;align-items:center;gap:14px}
.offer.popular{left:180px}
.offer.special{left:470px}
.offer-text{width:140px;text-align:center}
.offer-text h3{font-family:"Oswald",Arial,sans-serif;font-size:15px;font-weight:600}
.offer-text p{font-size:6.5px;line-height:1.5;color:var(--grey-text);margin:6px 0 8px}
.offer .thumb{width:84px;height:84px;border-radius:50%}

/* footer */
.footer{position:absolute;top:1112px;left:0;width:831px;height:88px;background:var(--teal-dark);text-align:center;padding-top:12px}
.social{display:flex;justify-content:center;gap:8px;margin-bottom:8px}
.social span{width:14px;height:14px;border-radius:50%;background:var(--white)}
.footer p{font-size:7px;line-height:1.6;color:#d9e6e7}
.footer .copy{font-size:6px;opacity:.7;margin-top:2px}
</style>
</head>
<body>

<header class="hero">
  <div class="hero-photo" role="img" aria-label="Makeup artist applying makeup to a client, soft pink and green tones"></div>
  <div class="topbar">
    <div class="brand">Fern and Fable</div>
    <ul class="nav">
      <li class="active">Home</li><li>About</li><li>Services</li><li>Prices</li><li>Blog</li><li>Gallery</li><li>Contact</li>
    </ul>
  </div>
  <div class="hero-copy">
    <h1>Lorem ipsum is simply dummy text</h1>
    <p>Lorem ipsum is simply dummy</p>
    <span class="btn">Read more</span>
  </div>
</header>

<section class="about">
  <div class="feature">
    <div class="icon"><svg width="20" height="20" viewBox="0 0 20 20"><circle cx="10" cy="7" r="4" fill="none" stroke="#3aa56a" stroke-width="2"/><path d="M3 18c1-4 4-6 7-6s6 2 7 6" fill="none" stroke="#3aa56a" stroke-width="2"/></svg></div>
    <h3>WHO <span>WE</span> ARE</h3>
    <p>Lorem ipsum is simply dummy text of the printing and typesetting industry, it has been the standard text.</p>
    <span class="btn">Read more</span>
  </div>
  <div class="feature">
    <div class="icon"><svg width="20" height="20" viewBox="0 0 20 20"><path d="M4 16l8-8 3 3-8 8H4z" fill="#3aa56a"/><path d="M13 4l3 3" stroke="#3aa56a" stroke-width="2"/></svg></div>
    <h3>WHAT <span>WE</span> DO</h3>
    <p>Lorem ipsum is simply dummy text of the printing and typesetting industry, it has been the standard text.</p>
    <span class="btn">Read more</span>
  </div>
  <div class="feature">
    <div class="icon"><svg width="20" height="20" viewBox="0 0 20 20"><rect x="3" y="5" width="14" height="11" rx="1" fill="none" stroke="#3aa56a" stroke-width="2"/><path d="M6 11l3 2 5-5" fill="none" stroke="#3aa56a" stroke-width="2"/></svg></div>
    <h3>HOW <span>IT</span> WORKS</h3>
    <p>Lorem ipsum is simply dummy text of the printing and typesetting industry, it has been the standard text.</p>
    <span class="btn">Read more</span>
  </div>
</section>

<section class="news">
  <svg class="news-photo" viewBox="0 0 831 222" preserveAspectRatio="none">
    <defs><linearGradient id="spa" x1="0" y1="0" x2="1" y2="1"><stop offset="0" stop-color="#6b4a3a"/><stop offset=".5" stop-color="#c9a087"/><stop offset="1" stop-color="#8c6b5a"/></linearGradient></defs>
    <polygon points="0,0 475,0 420,222 0,222" fill="url(#spa)" role="img" aria-label="Woman relaxing during a facial treatment at a spa"/>
    <polygon points="0,0 831,0 831,12 0,30" fill="var(--charcoal)"/>
  </svg>
  <div class="news-panel">
    <h2>Latest News</h2>
    <div class="news-item">
      <div class="date"><b>20</b><small>FEB</small></div>
      <div><p>Lorem ipsum is simply dummy text of the printing and typesetting industry standard.</p><a>READ MORE »</a></div>
    </div>
    <div class="news-item">
      <div class="date"><b>25</b><small>FEB</small></div>
      <div><p>Lorem ipsum is simply dummy text of the printing and typesetting industry standard.</p><a>READ MORE »</a></div>
    </div>
  </div>
</section>

<section class="services">
  <h2>Popular Services</h2>
  <p class="sub">Lorem ipsum is simply dummy text of the printing</p>
  <div class="rule"></div>
  <div class="cards">
    <div class="card">
      <div class="thumb" role="img" aria-label="Beauty service image in pink and teal" style="background:radial-gradient(circle at 35% 35%,#f2a0c0,#c2457e 55%,#2a8f9a)"></div>
      <p>Lorem ipsum is simply dummy text of the printing and typesetting industry standard text.</p>
      <span class="btn">Read more</span>
    </div>
    <div class="card dark">
      <div class="thumb" role="img" aria-label="Beauty service image in purple and dark tones" style="background:radial-gradient(circle at 50% 40%,#d8d2e6,#6d5f8f 50%,#2b2436)"></div>
      <p>Lorem ipsum is simply dummy text of the printing and typesetting industry standard text.</p>
      <span class="btn grey">Read more</span>
    </div>
    <div class="card teal">
      <div class="thumb" role="img" aria-label="Beauty service image in orange and pink" style="background:radial-gradient(circle at 40% 40%,#ffb04a,#f0513e 50%,#b2327c)"></div>
      <p>Lorem ipsum is simply dummy text of the printing and typesetting industry standard text.</p>
      <span class="btn teal">Read more</span>
    </div>
  </div>
</section>

<section class="offers">
  <div class="offer popular">
    <div class="offer-text">
      <h3>Most Popular</h3>
      <p>Lorem ipsum is simply dummy text of the printing and typesetting industry. It has been the standard text ever since.</p>
      <span class="btn">Read more</span>
    </div>
    <div class="thumb" role="img" aria-label="Popular beauty treatment image" style="background:radial-gradient(circle at 40% 40%,#c58a6e,#6a3e35 70%)"></div>
  </div>
  <div class="offer special">
    <div class="offer-text">
      <h3>Special Offer</h3>
      <p>Lorem ipsum is simply dummy text of the printing and typesetting industry. It has been the standard text ever since.</p>
      <span class="btn">Read more</span>
    </div>
    <div class="thumb" role="img" aria-label="Special offer beauty image in red" style="background:radial-gradient(circle at 45% 45%,#f07a7a,#c41c2c 65%)"></div>
  </div>
</section>

<footer class="footer">
  <div class="social"><span></span><span></span></div>
  <p>contact@fern-andfable.com</p>
  <p>0491 570 156</p>
  <p class="copy">Copyright © Fern and Fable. All rights reserved.</p>
</footer>

</body>
</html>
```